Banner Ad Design Project

I need a banner design for a new application which is going to the displayed on the ToolBazaar.

The banner is needed for this application:
https://pages.vendorhub-example.com/toolbazaar/itemView?itemId=q7R52000008kmpwXBB

Example banners can be found here:
https://pages.vendorhub-example.com/toolbazaar/itemView?itemId=q7R52000003htzsXBB

Or
https://pages.vendorhub-example.com/toolbazaar/itemView?itemId=q7R52000008wFKPXB4

Target Market(s)

Enterprise business.

Requirements
Must have
• Must include our pivotworks logo.

```html
<!DOCTYPE html>
<html lang="en">
<head>
<meta charset="utf-8">
<title>PivotWorks – Approval History Reporting</title>
<link href="https://fonts.googleapis.com/css2?family=Share+Tech&family=Electrolize&family=Nunito:wght@600&display=swap" rel="stylesheet">
<style>
  :root {
    --band-dark: #0a2452;
    --band-mid: #1d4a86;
    --band-light: #3a6aa8;
    --title-cyan: #46d2f4;
    --title-glow: rgba(70, 210, 244, 0.55);
    --tagline: #c9d5e6;
    --panel-white: #ffffff;
    --panel-edge: #9bb4d4;
    --brand-blue: #2f6fb8;
    --brand-dot: #f39a1e;
    --date-text: #2a3a55;
    --date-strip: rgba(255, 255, 255, 0.9);
    --tick-green: #2c9b2c;
    --cross-red: #d42424;
  }
  * { margin: 0; padding: 0; box-sizing: border-box; }
  html, body { width: 1200px; height: 103px; overflow: hidden; background: #fff; }

  .banner {
    position: relative;
    width: 1200px;
    height: 103px;
    overflow: hidden;
    background:
      linear-gradient(180deg, rgba(255,255,255,0.10) 0%, rgba(255,255,255,0) 45%, rgba(0,0,0,0.18) 100%),
      linear-gradient(90deg, var(--band-dark) 0%, var(--band-mid) 45%, var(--band-light) 80%, #6f95c6 100%);
  }

  .brand-panel {
    position: absolute;
    left: 0; top: 0;
    width: 300px; height: 103px;
  }
  .brand-panel svg { position: absolute; inset: 0; }
  .brand {
    position: absolute;
    left: 30px; top: 36px;
    display: flex; align-items: center; gap: 10px;
  }
  .brand-mark {
    width: 26px; height: 26px; border-radius: 50%;
    background: var(--brand-dot);
  }
  .brand-name {
    font-family: "Nunito", sans-serif;
    font-weight: 600;
    font-size: 24px;
    color: var(--brand-blue);
  }

  .headline {
    position: absolute;
    left: 318px; top: 2px;
    font-family: "Share Tech", sans-serif;
    font-weight: 400;
    font-size: 56px;
    line-height: 64px;
    letter-spacing: 1.5px;
    color: var(--title-cyan);
    text-shadow: 0 0 6px var(--title-glow), 1px 2px 2px rgba(0,0,0,0.5);
    white-space: nowrap;
  }

  .tagline {
    position: absolute;
    left: 380px; top: 64px;
    display: flex; align-items: center; gap: 14px;
    font-family: "Electrolize", sans-serif;
    font-size: 27px;
    line-height: 32px;
    color: var(--tagline);
    text-shadow: 1px 1px 2px rgba(0,0,0,0.45);
    white-space: nowrap;
  }
  .tagline .cube { width: 22px; height: 22px; }

  .viewer-photo {
    position: absolute;
    right: 0; top: 0;
    width: 100px; height: 103px;
    background: linear-gradient(180deg, #c9b7a4 0%, #a8927c 40%, #6f7786 100%);
    z-index: 1;
  }

  .date-log {
    position: absolute;
    left: 1040px; top: 0;
    width: 156px; height: 103px;
    display: flex; flex-direction: column; justify-content: space-around;
    padding: 8px 0;
    z-index: 2;
  }
  .date-row {
    display: flex; align-items: center; justify-content: flex-end; gap: 6px;
    height: 22px;
    padding-right: 4px;
    background: linear-gradient(90deg, rgba(255,255,255,0) 0%, var(--date-strip) 35%);
    font-family: "Electrolize", sans-serif;
    font-size: 11px;
    color: var(--date-text);
    white-space: nowrap;
  }
  .date-row svg { width: 14px; height: 14px; flex: none; }
</style>
</head>
<body>
<div class="banner">

  <div class="brand-panel">
    <svg width="300" height="103" viewBox="0 0 300 103" aria-hidden="true">
      <path d="M0 0 H250 Q285 51 250 103 H0 Z" fill="var(--panel-white)"/>
      <path d="M250 0 Q285 51 250 103" fill="none" stroke="var(--panel-edge)" stroke-width="3"/>
    </svg>
    <div class="brand">
      <span class="brand-mark"></span>
      <span class="brand-name">PivotWorks</span>
    </div>
  </div>

  <h1 class="headline">Approval History Reporting</h1>

  <div class="tagline">
    <span>Monitoring</span>
    <svg class="cube" viewBox="0 0 20 20" aria-hidden="true">
      <path d="M10 1 L18 5.5 L10 10 L2 5.5 Z" fill="#e6edf6"/>
      <path d="M2 5.5 L10 10 L10 19 L2 14.5 Z" fill="#a9b8cc"/>
      <path d="M18 5.5 L10 10 L10 19 L18 14.5 Z" fill="#7f91aa"/>
    </svg>
    <span>Tracking</span>
    <svg class="cube" viewBox="0 0 20 20" aria-hidden="true">
      <path d="M10 1 L18 5.5 L10 10 L2 5.5 Z" fill="#e6edf6"/>
      <path d="M2 5.5 L10 10 L10 19 L2 14.5 Z" fill="#a9b8cc"/>
      <path d="M18 5.5 L10 10 L10 19 L18 14.5 Z" fill="#7f91aa"/>
    </svg>
    <span>Approving</span>
  </div>

  <div class="viewer-photo" role="img" aria-label="Photo of a businesswoman looking through binoculars"></div>

  <div class="date-log">
    <div class="date-row"><span>29 march 2012</span>
      <svg viewBox="0 0 16 16" aria-label="rejected"><rect x="1" y="1" width="14" height="14" fill="#fff" stroke="#888"/><path d="M4 4 L12 12 M12 4 L4 12" stroke="var(--cross-red)" stroke-width="2.4"/></svg>
    </div>
    <div class="date-row"><span>30 march 2012</span>
      <svg viewBox="0 0 16 16" aria-label="approved"><rect x="1" y="1" width="14" height="14" fill="#fff" stroke="#888"/><path d="M3 8 L7 12 L15 2" fill="none" stroke="var(--tick-green)" stroke-width="2.6"/></svg>
    </div>
    <div class="date-row"><span>31 march 2012</span>
      <svg viewBox="0 0 16 16" aria-label="rejected"><rect x="1" y="1" width="14" height="14" fill="#fff" stroke="#888"/><path d="M4 4 L12 12 M12 4 L4 12" stroke="var(--cross-red)" stroke-width="2.4"/></svg>
    </div>
  </div>

</div>
</body>
</html>
```